The Wellness Barn Business Card

Info for the front..... (in whichever order and layout looks best)
Tara Pellworth
Physiotherapist
4/38 Upper Ridgeway Rd
Kelmoor Heights
QLD 4718
0462875309
tarapellworth47@mailnest.com
www.thewelnesbarn.com.au
on the back I would like to be able to write appointments so probably just that heading with lines.
I like a sort of rustic style but mostly professional, colours in naturals, beige, brown, green etc. I dont mind if the logo colour is changed slightly to suit.

```html
<!DOCTYPE html>
<html lang="en">
<head>
<meta charset="utf-8">
<title>The Wellness Barn – Business Card</title>
<link rel="stylesheet" href="https://fonts.googleapis.com/css2?family=Montserrat:wght@400;600;700&display=swap">
<style>
  :root {
    --forest: #2c4722;
    --paper: #ffffff;
    --ink: #333333;
    --backdrop: #2a2a2a;
  }
  * { margin: 0; padding: 0; box-sizing: border-box; }
  html, body {
    width: 1200px; height: 1059px; overflow: hidden;
    background: var(--backdrop);
    font-family: "Montserrat", Arial, sans-serif;
  }
  .card {
    position: absolute;
    width: 692px; height: 394px;
    background: var(--paper);
    overflow: hidden;
  }
  .card--back { left: 254px; top: 89px; }
  .card--front { left: 254px; top: 547px; }

  /* back side */
  .back-band {
    position: absolute; left: 0; top: 0; width: 100%; height: 125px;
    background: var(--forest);
    display: flex; align-items: center; justify-content: center;
  }
  .brand-name--band {
    color: var(--paper); font-weight: 700; font-size: 30px; letter-spacing: 0.5px;
  }
  .back-strip {
    position: absolute; left: 0; top: 130px; width: 100%; height: 6px;
    background: var(--forest);
  }
  .back-tab { position: absolute; left: 193px; top: 130px; width: 308px; height: 35px; }
  .back-heading {
    position: absolute; left: 193px; top: 130px; width: 308px; height: 35px;
    display: flex; align-items: center; justify-content: center;
    color: var(--paper); font-weight: 700; font-size: 22px; letter-spacing: 0.5px;
  }
  .write-line {
    position: absolute; left: 26px; top: 305px; width: 640px; height: 2px;
    background: var(--forest);
  }

  /* front side */
  .brand-block {
    position: absolute; left: 36px; top: 98px; width: 254px; height: 202px;
    display: flex; flex-direction: column; align-items: center; justify-content: center;
    color: var(--forest); font-weight: 700; text-align: center; line-height: 1.05;
  }
  .brand-block span { font-size: 44px; }
  .divider {
    position: absolute; left: 316px; top: 75px; width: 2px; height: 247px;
    background: var(--forest);
  }
  .details { position: absolute; left: 342px; top: 70px; color: var(--ink); }
  .person-name { color: var(--forest); font-weight: 700; font-size: 31px; line-height: 1.2; }
  .person-role { font-size: 18px; margin-top: 2px; }
  .address { font-size: 18px; line-height: 27.5px; margin-top: 16px; }
  .contact { list-style: none; font-size: 18px; margin-top: 14px; }
  .contact li { display: flex; align-items: center; gap: 8px; height: 27px; }
  .contact svg { width: 14px; height: 14px; fill: var(--forest); flex: none; }
</style>
</head>
<body>

<section class="card card--back" aria-label="Back of card">
  <div class="back-band"><span class="brand-name--band">The Wellness Barn</span></div>
  <div class="back-strip"></div>
  <svg class="back-tab" viewBox="0 0 308 35" aria-hidden="true">
    <polygon points="0,0 308,0 279,35 30,35" fill="var(--forest)"/>
  </svg>
  <div class="back-heading">APPOINTMENTS</div>
  <div class="write-line"></div>
</section>

<section class="card card--front" aria-label="Front of card">
  <div class="brand-block"><span>The</span><span>Wellness</span><span>Barn</span></div>
  <div class="divider"></div>
  <div class="details">
    <h1 class="person-name">Tara Pellworth</h1>
    <p class="person-role">Physiotherapist</p>
    <p class="address">4/38 Upper Ridgeway Rd<br>Kelmoor Heights<br>QLD 4718</p>
    <ul class="contact">
      <li><svg viewBox="0 0 16 16"><path d="M2 6c0-2 2-3 6-3s6 1 6 3v1h-3V6H5v1H2z M4 8h8l1 5H3z"/></svg>0462875309</li>
      <li><svg viewBox="0 0 16 16"><path d="M1 4h14v1L8 9 1 5z M1 6.5l7 4 7-4V12H1z"/></svg>tarapellworth47@mailnest.com</li>
      <li><svg viewBox="0 0 16 16"><circle cx="8" cy="8" r="7"/></svg>www.thewelnesbarn.com.au</li>
    </ul>
  </div>
</section>

</body>
</html>
```